Community coffee table book/quiz book

I need a couple of things for my book:
- Book cover (Title: "Quizbok om Kvernlia")
- "Cover pages" for each chapter of the book (15-16 chapters)
- "Watermark" or background design for all the pages of the book.
- A cover image for the book's Kettlebook page.
- Design of a paper "belt"

The book:
The book will consist of about 200+ pages with ten questions on one page and ten answers on the next.

The name of the book is "Quizbok om Kvernlia" which means 1000 questions about Fyllingsdalen (Fyllingsdalen is a suburb of the city Bergen in Norway). Author is Tore Halvik.
The questions in the book are grouped in chapters like:
History
Facts
Schools
Businesses
People/profiles
Sport
Culture
Buildings/Landmarks/Sculptures
The different areas of the suburb
The city
Language/expressions
Nature
The names of the chapters are not set, so it would be good to have the option to change the title of the pages without having to contact the designer (maybe by adding the text on top of the cover page?). I therefore suggest that these images are without text.
The book size is 18X18 cm.

The chapter cover pages:
The book will basically consist of text. Ten questions on one page, and ten questions on the next. Visually it will be quite "boring" to look at. I would therefore like to have a chapter cover page for each chapter, preferable in colour.

Water mark:
To avoid having a book full of white pages with limited amount of text I thought of having some kind of design on each page. I do not know how this should be done, but maybe it is possible to create some kind of background image or watermark image with similar design as the book cover and the chapter covers?

The Kettlebook cover image:
This should be the same as, or similar to, the book cover.
I believe the optimal size is 828px x 315px?

Paper "belt":
The book is to be sold for charity. The receiver of the money is the local sports club. I would like to have the book "wrapped in a 5-6 cm wide paper belt with the logo of the sports club (please see logo and colours here: http://www.ilbrattmo.example). I do not think that the book cover itself should have the sports club's color (purple), but maybe the paper band could? (Again: YOU are the designer)

Photos:
I reckon you would like some photos for both the book cover and the chapter covers. I will of course do the best I can to provide these photos when I have selected a designer. I the meantime

Target Market(s)

Target market is middle clas men and women 35+ from the geographical area Fyllingsdalen.

Industry/Entity Type

Community

Font styles to use
Serif
Sans Serif

Requirements
Must have
• The book will be sold by children on doors. The buyers will probably take a look briefly through the book and then decide if they are going to buy.
• It is important that they like the question types, categories and some of the actual questions they read. But it is also important that they like the look of the book. Therefore the book cover and the chapter cover pages must be appealing enough for the buyers to want this book on theor coffee table.
Nice to have
• I have uploaded a short video clip to VidPlaza (https://www.vidplaza.example/watch?v=qoz4Tr7wnLx). This a promo clip from Pimbo Kanal. I felt inspired when I saw it and thought that backgrounds like the ones used in the promo could also be used as backgrounds for each chapter's cover pages. Maybe different colour for each chapter? Screenshots from the clip is uploaded below.
• Then again: Maybe I am an idiot? YOU are the designer :-)
Should not have
• There has been some rivalry between two sportsclubs in the region after the clubs was merged a couple of years ago. I therefore believe we should therefore try avoid both the old clubs' colours (blue&yellow and green) and the new club's colour (purple).

```html
<!DOCTYPE html>
<html lang="no">
<head>
<meta charset="utf-8">
<title>Quizbok om Kvernlia – design set</title>
<link rel="stylesheet" href="https://fonts.googleapis.com/css2?family=Arimo:wght@400;700&family=Black+Ops+One&family=Lobster&family=Oswald:wght@400;700&display=swap">
<style>
  :root{
    --paper:#ffffff;
    --ink:#000000;
    --pale-yellow:#fddf7c;
    --amber:#f7a01b;
    --flame:#f15a24;
    --gold:#ffc20e;
    --charcoal:#231f20;
    --white:#ffffff;
    --wm-pale:#eeeeee;
    --wm-band:#6b6b6b;
    --wm-field:#e5e5e5;
    --wm-tab:#2e2e2e;
    --wm-text:#333333;
  }
  html,body{margin:0;padding:0;overflow:hidden;background:var(--paper);}
  .canvas{position:relative;width:1200px;height:1000px;overflow:hidden;background:var(--paper);}
  .piece{position:absolute;display:block;}
  .book-cover{left:40px;top:35px;width:420px;height:420px;}
  .social-cover{left:550px;top:180px;width:600px;height:260px;}
  .chapter-history{left:30px;top:538px;width:370px;height:380px;}
  .chapter-culture{left:420px;top:538px;width:370px;height:380px;}
  .page-watermark{left:800px;top:538px;width:370px;height:380px;}

  .pale{fill:var(--pale-yellow);}
  .amber{fill:var(--amber);}
  .flame{fill:var(--flame);}
  .tab{fill:var(--gold);opacity:.72;}
  .plate{fill:var(--gold);opacity:.6;}
  .wm-pale{fill:var(--wm-pale);}
  .wm-band{fill:var(--wm-band);}
  .wm-field{fill:var(--wm-field);}
  .wm-tab{fill:var(--wm-tab);opacity:.8;}

  .title-kicker{font-family:"Arimo",Arial,sans-serif;font-weight:700;fill:var(--white);letter-spacing:3px;}
  .title-place{font-family:"Oswald","Arial Narrow",sans-serif;font-weight:700;fill:var(--charcoal);letter-spacing:1px;}
  .author{font-family:"Arimo",Arial,sans-serif;font-weight:700;fill:var(--white);}
  .chapter-stencil{font-family:"Black Ops One",system-ui,sans-serif;fill:var(--charcoal);}
  .chapter-script{font-family:"Lobster",cursive;fill:var(--white);}
  .question{font-family:"Arimo",Arial,sans-serif;fill:var(--wm-text);font-size:11px;}

  .label{position:absolute;margin:0;font-family:"Oswald","Arial Narrow",sans-serif;font-weight:400;font-size:44px;line-height:50px;color:var(--ink);text-align:center;white-space:nowrap;letter-spacing:-.5px;}
  .label-book{left:105px;top:458px;width:300px;}
  .label-social{left:590px;top:458px;width:540px;}
  .label-chapters{left:220px;top:918px;width:360px;}
  .label-watermark{left:850px;top:918px;width:300px;}
</style>
</head>
<body>
<main class="canvas">

  <svg class="piece book-cover" viewBox="40 35 420 420" aria-label="Book cover: Quizbok om Kvernlia">
    <polygon class="pale" points="58,48 438,44 438,440 58,446"/>
    <rect class="amber" x="58" y="55" width="380" height="380"/>
    <rect class="flame" x="58" y="95" width="380" height="298"/>
    <polygon class="tab" points="332,55 445,76 436,126 326,105"/>
    <polygon class="tab" points="62,363 168,386 160,434 52,412"/>
    <rect class="plate" x="130" y="142" width="245" height="150"/>
    <polygon class="plate" points="124,170 376,158 378,268 128,282"/>
    <polygon class="plate" points="140,140 370,150 366,296 136,290"/>
    <text class="title-kicker" x="252" y="192" font-size="20" text-anchor="middle">QUIZBOK OM</text>
    <text class="title-place" x="252" y="260" font-size="52" text-anchor="middle">KVERNLIA</text>
    <text class="author" x="252" y="330" font-size="12" text-anchor="middle">Tore Halvik</text>
  </svg>

  <svg class="piece social-cover" viewBox="550 180 600 260" aria-label="Kettlebook cover image">
    <polygon class="pale" points="568,196 1135,190 1135,424 568,430"/>
    <rect class="amber" x="572" y="200" width="558" height="220"/>
    <rect class="flame" x="572" y="240" width="558" height="138"/>
    <polygon class="tab" points="976,200 1138,222 1131,270 970,250"/>
    <polygon class="tab" points="566,348 728,372 722,418 560,395"/>
    <rect class="plate" x="768" y="236" width="166" height="120"/>
    <polygon class="plate" points="762,256 936,248 936,330 766,340"/>
    <polygon class="plate" points="774,236 932,244 928,356 770,352"/>
    <text class="title-kicker" x="851" y="278" font-size="14" text-anchor="middle">QUIZBOK OM</text>
    <text class="title-place" x="851" y="328" font-size="38" text-anchor="middle">KVERNLIA</text>
  </svg>

  <svg class="piece chapter-history" viewBox="30 538 370 380" aria-label="Chapter cover: History">
    <polygon class="pale" points="48,551 385,548 385,905 48,908"/>
    <rect class="amber" x="48" y="560" width="337" height="336"/>
    <rect class="flame" x="48" y="600" width="337" height="258"/>
    <polygon class="tab" points="293,560 392,579 384,626 286,606"/>
    <polygon class="tab" points="48,830 148,852 140,898 42,878"/>
    <rect class="plate" x="112" y="636" width="218" height="142"/>
    <polygon class="plate" points="106,660 332,650 334,756 110,768"/>
    <polygon class="plate" points="120,634 326,644 322,780 116,774"/>
    <text class="chapter-stencil" x="220" y="734" font-size="46" text-anchor="middle">HISTORY</text>
  </svg>

  <svg class="piece chapter-culture" viewBox="420 538 370 380" aria-label="Chapter cover: Culture">
    <polygon class="pale" points="438,551 775,548 775,905 438,908"/>
    <rect class="amber" x="438" y="560" width="337" height="336"/>
    <rect class="flame" x="438" y="600" width="337" height="258"/>
    <polygon class="tab" points="683,560 782,579 774,626 676,606"/>
    <polygon class="tab" points="438,830 538,852 530,898 432,878"/>
    <rect class="plate" x="502" y="636" width="218" height="142"/>
    <polygon class="plate" points="496,660 722,650 724,756 500,768"/>
    <polygon class="plate" points="510,634 716,644 712,780 506,774"/>
    <text class="chapter-script" x="610" y="730" font-size="58" text-anchor="middle">Culture</text>
  </svg>

  <svg class="piece page-watermark" viewBox="800 538 370 380" aria-label="Page background with question list">
    <polygon class="wm-pale" points="820,551 1157,548 1157,905 820,908"/>
    <rect class="wm-band" x="820" y="548" width="337" height="360"/>
    <rect class="wm-field" x="820" y="598" width="337" height="260"/>
    <polygon class="wm-tab" points="1063,558 1160,578 1151,628 1055,608"/>
    <polygon class="wm-tab" points="820,833 919,855 911,901 813,880"/>
    <text class="question" x="870" y="625">1. Sakldjs asdlkjsd sahjdsdkh sajsdalhksda</text>
    <text class="question" x="870" y="649">2. Asjknddfkj dekjhffjh dskjfhsdfjkhdsfjkhskjsd</text>
    <text class="question" x="870" y="673">3. Qdlkfsjs dslkjfisdfklj sdlkfjdlkfjsdlkfj dksjfldslkj</text>
    <text class="question" x="870" y="697">4. Bsadlkjdlk sljkdslkdj slkjdklajsdl asdksjd</text>
    <text class="question" x="870" y="721">5. Lsdkjhga sadhjgasdhui eguwbn jhewvrlskjueh</text>
    <text class="question" x="870" y="745">6. Wdekjhfs sdkjhffoi edfukiho rouifhoirf</text>
    <text class="question" x="870" y="769">7. Mfjscfkjds dkjshbiu riugfhrgjnb fdndf;lelruhr</text>
    <text class="question" x="870" y="793">8. Bsdklfjsofij dihjfiojf id dfij dfj fodfjdofj fddi</text>
    <text class="question" x="870" y="817">9. Kjdskflkdfsh duhfd hfduhdf difdoiddihd j diud</text>
    <text class="question" x="870" y="841">10. Gslhjkfd sdufhg fiuf dkjhd du fuhyudhuhyuh</text>
  </svg>

  <p class="label label-book">BOOK COVER</p>
  <p class="label label-social">KETTLEBOOK COVER PHOTO</p>
  <p class="label label-chapters">COVER PAGES</p>
  <p class="label label-watermark">WATERMARK</p>

</main>
</body>
</html>
```